Accountant website

Please design a accountant website for www.quillbrookadvisory.com.au. This site is majorly out of date, and is not supported by modern browsers.

The style should use the reds from the design at dev.quillbrookadvisory.com.au, and should be modern and make use of Slides (large content slides that the user scrolls through on the front page).

The content is largely already on the site, however happy to move some around to suit the modern design as required.

The dev.quillbrookadvisory.com.au was a rough mock up that I have completed that the client is "happy" with the direction, however this needs a lot of polish and finishing touches, and I will accept designs that differ from this, but highly recommend that this is used as a guide.

Ready to be sliced PSD Only - HTML no required.

In all honesty, although I can technically do a lot of this, the polished finished I want for this site has eluded me in a few attempts, and therefore I am looking out there at you much more artistic people to finish (or redesign if required) this site.

Target Market(s)

Higher end Small - Medium Business

Industry/Entity Type

Accountant

Requirements
Must have
• Must use the logo from dev.quillbrookadvisory.com.au use exactly the red colours as defined in this layout. A basic layout PSD (to get the colour etc) and the logo in ai format is attached to this project. Please ignore the SSL warning on the development site.

The final product does NOT have to be the same as shown on dev.quillbrookadvisory.com.au however the red colour scheme must be used. The client DOES want the logo on the RIGHT.

Must have a front landing page design, and a page layout that considers the other page content (at least one separate PSD)
Nice to have
• I really am looking at a slide format for the front page simular to:

http://www.plumvane.com/au/
http://www.tessaform.com/

The attached photos should be used on the site. Was considering a rotating banner with these images are a watermark background on a solid Red header bar, but happy to be shown other options.
Should not have
• Please no "Layout Goblin" submissions.

```html
<!DOCTYPE html>
<html lang="en">
<head>
<meta charset="utf-8">
<title>Quillbrook Advisory</title>
<link href="https://fonts.googleapis.com/css2?family=Ubuntu:wght@400;500;700&family=Open+Sans:wght@600;700&family=Arimo:wght@400&display=swap" rel="stylesheet">
<style>
:root{
  --red:#d71920;
  --ink:#2f2f2f;
  --grey:#6d6d6d;
  --soft:#8a8a8a;
  --line:#e3e3e3;
  --hero-a:#f5f1e7;
  --hero-b:#ebe4d4;
  --photo-a:#e2cdc6;
  --photo-b:#c48480;
  --dark:#2c2c2c;
}
*{margin:0;padding:0;box-sizing:border-box}
html,body{width:1107px;height:1200px;overflow:hidden;background:#fff}
body{position:relative;font-family:"Ubuntu",sans-serif;color:var(--ink)}
.abs{position:absolute}
.topbar{left:0;top:0;width:1107px;height:4px;background:var(--red)}
.header{left:0;top:4px;width:1107px;height:103px;background:#fff;box-shadow:0 2px 4px rgba(0,0,0,.08);z-index:2}
.social{top:21px;width:29px;height:29px;background:var(--dark)}
.contact{top:29px;font-size:9.5px;color:var(--grey)}
.contact b{font-weight:400;color:var(--ink)}
.nav-rule{left:75px;top:67px;width:442px;height:1px;background:var(--line)}
.nav-active{left:75px;top:66px;width:39px;height:2px;background:var(--red)}
.nav a{position:absolute;top:74px;font-size:9.5px;color:#555;text-decoration:none}
.brand{left:822px;top:34px;display:flex;align-items:center;gap:8px}
.brand-name{font-family:"Open Sans",sans-serif;font-weight:700;font-size:26px;line-height:1;color:var(--ink);letter-spacing:-.5px}
.brand-sub{font-family:"Open Sans",sans-serif;font-weight:700;font-size:11px;color:var(--ink);letter-spacing:.3px;margin-top:3px}
.brand-mark{width:22px;height:22px;background:var(--red)}
.hero{left:0;top:107px;width:1107px;height:441px;background:radial-gradient(ellipse at 50% 45%,var(--hero-a),var(--hero-b))}
.hero-rule{left:0;top:548px;width:1107px;height:3px;background:var(--red)}
.hero-title{left:97px;top:212px;font-family:"Open Sans",sans-serif;font-weight:700;font-size:26px;color:var(--ink);letter-spacing:.3px;display:flex;align-items:center}
.hero-title span{background:#ddd8cc;color:var(--red);padding:1px 11px 1px 6px;margin-left:4px}
.hero-box{left:95px;top:272px;width:310px;height:171px;border:3px solid #fff;padding:10px 10px}
.hero-box h2{font-family:"Open Sans",sans-serif;font-weight:600;font-size:18.5px;line-height:20px;color:var(--soft);letter-spacing:-.1px}
.hero-box p{margin-top:14px;font-size:9px;line-height:12.3px;color:#777;text-align:justify}
.arrow{top:320px;width:34px;height:33px;background:linear-gradient(#fff,#e9e9e9);border-radius:3px;box-shadow:0 1px 3px rgba(0,0,0,.25);display:flex;align-items:center;justify-content:center}
.hero-photo{left:484px;top:160px;width:443px;height:388px;border-radius:10px 10px 0 0;background:linear-gradient(180deg,var(--photo-a),var(--photo-b))}
.dots{left:515px;top:527px;width:80px;height:18px;background:rgba(255,255,255,.6);border-radius:3px;display:flex;align-items:center;gap:6px;padding-left:5px}
.dot{width:8px;height:8px;border-radius:50%;background:#ccc}
.dot.on{background:#555}
.h-section{font-family:"Open Sans",sans-serif;font-weight:700;font-size:19px;color:var(--ink);letter-spacing:.2px}
.h-section em{font-style:normal;color:var(--red)}
.feature-icon{left:55px;width:47px;height:47px;border:1px solid #555;display:flex;align-items:center;justify-content:center}
.feature-title{left:116px;font-size:14px;color:var(--ink)}
.feature-text{left:116px;width:228px;font-size:11px;line-height:17.2px;color:var(--grey)}
.about{left:426px;width:520px;font-size:11px;line-height:17.2px;color:var(--grey)}
.signature{left:426px;top:894px;width:95px;height:30px;background:linear-gradient(90deg,#f6d7d8,#fbeced)}
.role{left:426px;top:947px;font-size:9px;color:var(--ink)}
.divider{left:59px;top:1004px;width:925px;height:1px;background:var(--line)}
.h-col{font-size:16px}
.col-text{width:282px;font-family:"Arimo",sans-serif;font-size:11.6px;line-height:18px;color:var(--grey)}
.col-link{font-family:"Arimo",sans-serif;font-size:11.6px;color:var(--red)}
.monitor{width:139px;height:103px}
.vrule{left:526px;top:1070px;width:1px;height:115px;background:var(--line)}
</style>
</head>
<body>
<div class="abs topbar"></div>

<header class="abs header">
  <div class="abs social" style="left:75px"></div>
  <div class="abs social" style="left:108px"></div>
  <div class="abs social" style="left:141px"></div>
  <div class="abs contact" style="left:244px">Email us: <b>hello@quillbrookmail.com</b></div>
  <div class="abs contact" style="left:425px">Call us: <b>+1 555 01 23</b></div>
  <div class="abs nav-rule"></div>
  <div class="abs nav-active"></div>
  <nav class="nav">
    <a style="left:75px">About us</a>
    <a style="left:137px">Services</a>
    <a style="left:192px">Working with us</a>
    <a style="left:284px">Testimonials</a>
    <a style="left:359px">Articl of the moment</a>
    <a style="left:465px">Client login</a>
  </nav>
  <div class="abs brand">
    <div>
      <div class="brand-name">QUILLBROOK</div>
      <div class="brand-sub">ADVISORY</div>
    </div>
    <div class="brand-mark"></div>
  </div>
</header>

<section class="abs hero"></section>
<div class="abs hero-photo" role="img" aria-label="Photo of a smiling consultant in a red shirt holding an open laptop"></div>
<h1 class="abs hero-title">BUSINESS <span>CAN BE HARD</span></h1>
<div class="abs hero-box">
  <h2>But we make detailed analysis<br>of your finances easy</h2>
  <p>Lorem Ipsum is simply dummy text of the printing and typesetting industry. Lorem Ipsum has been the industry's standard dummy text ever since the 1500s, when an unknown printer took a galley of type and scrambled it to make a type specimen book. It has survived not only five centuries, but also the leap into electronic typesetting, remaining essentially unchanged.</p>
</div>
<div class="abs arrow" style="left:11px"><svg width="8" height="10"><path d="M7 0v10L0 5z" fill="#aaa"/></svg></div>
<div class="abs arrow" style="left:1060px"><svg width="8" height="10"><path d="M1 0v10l7-5z" fill="#aaa"/></svg></div>
<div class="abs dots">
  <svg width="8" height="10"><path d="M0 0v10l8-5z" fill="#444"/></svg>
  <div class="dot on"></div><div class="dot"></div><div class="dot"></div>
  <svg width="6" height="10"><path d="M1 0v10M5 0v10" stroke="#999" stroke-width="1.3"/></svg>
</div>
<div class="abs hero-rule"></div>

<h2 class="abs h-section" style="left:56px;top:617px">OUR FEATURES</h2>

<div class="abs feature-icon" style="top:672px">
  <svg width="18" height="18" viewBox="0 0 18 18"><path d="M3 16L13 6" stroke="#d71920" stroke-width="3" stroke-linecap="round"/><path d="M14 1v3M12.5 2.5h3M5 2v2M4 3h2" stroke="#d71920" stroke-width="1"/></svg>
</div>
<div class="abs feature-title" style="top:672px">Integer Lobortis Cursus</div>
<div class="abs feature-text" style="top:694px">Aliquam quis quam placerat, dignissim massa in, posuere mi.</div>

<div class="abs feature-icon" style="top:762px">
  <svg width="18" height="18" viewBox="0 0 18 18"><circle cx="9" cy="9" r="6" fill="none" stroke="#d71920" stroke-width="4" stroke-dasharray="2.4 1.6"/><circle cx="9" cy="9" r="5" fill="#d71920"/><circle cx="9" cy="9" r="2" fill="#fff"/></svg>
</div>
<div class="abs feature-title" style="top:762px">Quisque Dignissim Nisi Diam</div>
<div class="abs feature-text" style="top:784px">Quis egestas magna porttitor ac. Fusce at tellus laoreet, accumsan purus in.</div>

<div class="abs feature-icon" style="top:852px">
  <svg width="20" height="18" viewBox="0 0 20 18"><rect x="1" y="1" width="18" height="12" fill="#d71920"/><rect x="3" y="3" width="14" height="8" fill="#fff" opacity=".25"/><rect x="8" y="13" width="4" height="3" fill="#d71920"/><rect x="5" y="16" width="10" height="1.5" fill="#d71920"/></svg>
</div>
<div class="abs feature-title" style="top:852px">Nunc Pulvinar Pellentesque</div>
<div class="abs feature-text" style="top:874px">Duis mollis nisi sit amet dolor malesuada hendrerit.</div>

<h2 class="abs h-section" style="left:422px;top:617px">GETTING TO KNOW QUILLBROOK <em>ADVISORY</em></h2>
<p class="abs about" style="top:672px">Fusce hendrerit, mi non lobortis pellentesquusce hendrerit, mi non lobortis pellentesque, nibh ante accumsan nisi, in tristique nibh nisi nec tortor.cumsan nisi, in tristique nibh nisi nec tortor. Mauris nibh sem, vulputate non consequat in, condimentm, vulputate non consequat in, condimentum eget nulla. Cras quis enim luctus, convallis libero nulla. Cras quis enim luctus, convallis libero non, tincidunt diam. Proin vestibulum libero massa, et moleam. Proin vestibulum libero massa, et molestie dui bibendum nec. Duis tincidunt sagittis tristiqubendum nec. Duis tincidunt sagittis tristique. Duis pulvinar nisl non sem tincidunt aliquam. Donulvinar nisl non sem tincidunt aliquam. Donec turpis erat, cursus et consectetur eu, interdum non velitrsus et consectetur eu, interdum non velit.</p>
<p class="abs about" style="top:828px">Ut sit amet libero velit. Praesent dignissim set sit amet libero velit. Praesent dignissim sem sapien, a vulputate enim auctor vitae. Duis non lorem lputate enim auctor vitae. Duis non lorem porta, adipiscing eros sit amet, tempor sem. dipiscing eros sit amet, tempor sem.</p>
<div class="abs signature" role="img" aria-label="Handwritten signature of Harlan Mews"></div>
<div class="abs role">MAGNIS Founder</div>

<div class="abs divider"></div>

<h3 class="abs h-section h-col" style="left:57px;top:1041px">BELIEVING IN THE HERE AND NOW</h3>
<p class="abs col-text" style="left:59px;top:1082px">Aliquam enim enim, pharetra in sodales at, interdum sit amet dui. Nullam vulputate euismod urna non pharetra. Phasellus blandit mattis ipsum, ac laoreet lorem lacinia et. Cras et ligula libero.</p>
<a class="abs col-link" style="left:59px;top:1170px">Haretra in sodales atsen interdum ›</a>
<div class="abs monitor" style="left:353px;top:1078px" role="img" aria-label="Desktop monitor showing two colleagues reviewing documents">
  <svg width="139" height="103" viewBox="0 0 139 103"><rect x="4" y="0" width="126" height="82" rx="2" fill="#2a2a2a"/><rect x="8" y="4" width="118" height="72" fill="#c9d6e0"/><rect x="4" y="82" width="126" height="7" fill="#cfcfcf"/><rect x="56" y="89" width="22" height="6" fill="#bbb"/><ellipse cx="67" cy="99" rx="60" ry="3" fill="#ddd"/></svg>
</div>

<div class="abs vrule"></div>

<h3 class="abs h-section h-col" style="left:579px;top:1041px">MONTHLY BILLING TO PLAN BY</h3>
<p class="abs col-text" style="left:580px;top:1082px;width:258px">Aliquam enim enim, pharetra in sodales at, interdum sit amet dui. Nullam vulputate euismod urna non pharetra. Phasellus blandit mattis ipsum, ac laoreet lorem lacinia et. Cras et ligula.</p>
<a class="abs col-link" style="left:580px;top:1170px">Haretra in sodales atsen interdum ›</a>
<div class="abs monitor" style="left:845px;top:1078px" role="img" aria-label="Desktop monitor showing a small team gathered around a laptop">
  <svg width="139" height="103" viewBox="0 0 139 103"><rect x="4" y="0" width="126" height="82" rx="2" fill="#2a2a2a"/><rect x="8" y="4" width="118" height="72" fill="#b98a92"/><rect x="4" y="82" width="126" height="7" fill="#cfcfcf"/><rect x="56" y="89" width="22" height="6" fill="#bbb"/><ellipse cx="67" cy="99" rx="60" ry="3" fill="#ddd"/></svg>
</div>
</body>
</html>
```